Humorous Book by Comedian Needs E-book Cover

My book 'A Kettle on the Porch' is on Leafpad but I want a better cover designed. Cover needs my photo on it. My name is the most important text (because I have an existing audience.)

Text elements:
Author: Dorvel Pim
Title: A Kettle on the Porch
Subtitle: Tenth Anniversary Edition
Review Quote: 'All of his columns are amusing. The best are masterpieces.' Harbour Ledger

Above my name it should say: Collected Humour From NZ's Award-Winning Comedian

Here's the present version (which is why I want an improved version!)
http://www.brightmart-example.com/A-Kettle-Porch-Anniversary-Edition-ebook/dp/Q77TX2M904

Book covers I admire:

http://www.brightmart-example.co.uk/Why-The-Fern-Odile-Brask-ebook/dp/Q3318ZR7LN/ref=tmm_kin_title_0

http://www.brightmart-example.com/Gravelhat-Mira-Dunst-ebook/dp/Q691PLE583/ref=tmm_kin_title_0

http://www.brightmart-example.co.uk/Why-Keep-Lantern-Rex-Palfrey-ebook/dp/Q58JN3TQ7V

Leafpad covers need to work as thumbnails, as well as on small device screens.

This cover is for Brightmart Leafpad. Tech specs are on Leafpad Direct Publishing page. Dimensions: Requirements for the size of your cover art have an ideal height/width ratio of 1.6, this means: • A minimum of 625 pixels on the shortest side and 1000 pixels on the longest side • For best quality, your image would be 2820 pixels on the shortest side and 4500 pixels on the longest side

Dimensions Requirements for the size of your cover art have an ideal height/width ratio of 1.6, this means: • A minimum of 625 pixels on the shortest side and 1000 pixels on the longest side • For best quality, your image would be 2820 pixels on the shortest side and 4500 pixels on the longest side

Comedian

```html
<!DOCTYPE html>
<html lang="en">
<head>
<meta charset="utf-8">
<title>Dorvel Pim – A Kettle on the Porch</title>
<link rel="stylesheet" href="https://fonts.googleapis.com/css2?family=Poiret+One&family=Josefin+Sans:ital,wght@0,300;0,400;1,400&family=Cinzel:wght@700&display=swap">
<style>
  :root {
    --bg-centre: #23735a;
    --bg-mid: #1f5c47;
    --bg-edge: #1a4433;
    --cream: #f7efe4;
    --white: #ffffff;
    --gold: #ecd0a6;
    --gold-line: #c9a46a;
    --shadow: rgba(10, 25, 20, 0.9);
    --hair: #2b2620;
    --skin: #b8876a;
    --shirt: #efe3d2;
    --suit-light: #f3bfa8;
    --suit-mid: #e4a690;
    --suit-dark: #c98774;
  }
  html, body {
    margin: 0;
    padding: 0;
    width: 752px;
    height: 1200px;
    overflow: hidden;
    background: var(--bg-edge);
  }
  .cover {
    position: relative;
    width: 752px;
    height: 1200px;
    overflow: hidden;
    background: radial-gradient(ellipse 70% 55% at 50% 52%, var(--bg-centre) 0%, var(--bg-mid) 55%, var(--bg-edge) 100%);
    font-family: "Poiret One", sans-serif;
    color: var(--cream);
    text-align: center;
  }
  .kicker {
    position: absolute;
    top: 32px;
    left: 0;
    right: 0;
    margin: 0;
    font-family: "Poiret One", sans-serif;
    font-size: 19px;
    letter-spacing: 0.4px;
    color: var(--cream);
    -webkit-text-stroke: 0.6px var(--cream);
  }
  .author {
    position: absolute;
    top: 52px;
    left: 0;
    right: 0;
    margin: 0;
    font-family: "Poiret One", sans-serif;
    font-weight: 400;
    font-size: 160px;
    line-height: 140px;
    letter-spacing: 4px;
    color: var(--cream);
    -webkit-text-stroke: 3px var(--cream);
    text-shadow: 0 4px 10px rgba(0,0,0,0.3);
  }
  .author span { display: block; }
  .author-photo {
    position: absolute;
    top: 280px;
    left: 120px;
    width: 540px;
    height: 680px;
  }
  .title {
    position: absolute;
    top: 942px;
    left: 0;
    right: 0;
    margin: 0;
    font-family: "Poiret One", sans-serif;
    font-weight: 400;
    font-size: 56px;
    line-height: 64px;
    color: var(--white);
    -webkit-text-stroke: 1.5px var(--white);
    text-shadow: 2px 3px 4px var(--shadow);
    white-space: nowrap;
  }
  .title .accent {
    border-bottom: 3px solid var(--gold-line);
  }
  .subtitle {
    position: absolute;
    top: 1010px;
    left: 0;
    right: 0;
    margin: 0;
    font-family: "Cinzel", serif;
    font-weight: 700;
    font-size: 22px;
    letter-spacing: 2.5px;
    color: var(--gold);
    text-shadow: 1px 1px 0 var(--shadow), -1px -1px 0 var(--shadow), 1px -1px 0 var(--shadow), -1px 1px 0 var(--shadow);
  }
  .review {
    position: absolute;
    top: 1070px;
    left: 0;
    right: 0;
    margin: 0;
    font-family: "Josefin Sans", sans-serif;
    font-weight: 300;
    color: var(--white);
  }
  .review-quote {
    margin: 0;
    font-size: 21px;
    line-height: 27px;
  }
  .review-source {
    display: block;
    margin-top: 2px;
    font-size: 20px;
  }
  .review-source cite { font-style: italic; font-weight: 400; }
</style>
</head>
<body>
  <main class="cover">
    <p class="kicker">Collected Humour from NZ’s Award-Winning Comedian</p>
    <h1 class="author"><span>DORVEL</span><span>PIM</span></h1>

    <svg class="author-photo" viewBox="0 0 540 680" role="img" aria-label="Portrait photo of the author smiling, wearing glasses, a peach dinner jacket and a dark bow tie">
      <defs>
        <linearGradient id="portraitTone" x1="0" y1="0" x2="0" y2="1">
          <stop offset="0%" stop-color="var(--hair)"/>
          <stop offset="10%" stop-color="var(--skin)"/>
          <stop offset="27%" stop-color="var(--skin)"/>
          <stop offset="36%" stop-color="var(--shirt)"/>
          <stop offset="55%" stop-color="var(--suit-light)"/>
          <stop offset="82%" stop-color="var(--suit-mid)"/>
          <stop offset="100%" stop-color="var(--suit-dark)"/>
        </linearGradient>
        <filter id="softEdge" x="-20%" y="-20%" width="140%" height="140%">
          <feGaussianBlur stdDeviation="14"/>
        </filter>
        <mask id="portraitMask">
          <path d="M165 30 Q270 -10 375 30 L385 210 Q520 230 525 330 L530 660 L10 660 L15 330 Q20 230 155 210 Z" fill="#fff" filter="url(#softEdge)"/>
        </mask>
      </defs>
      <rect x="0" y="0" width="540" height="680" fill="url(#portraitTone)" mask="url(#portraitMask)"/>
    </svg>

    <h2 class="title">A KETTLE <span class="accent">ON THE</span> PORCH</h2>
    <p class="subtitle">TENTH ANNIVERSARY EDITION</p>

    <blockquote class="review">
      <p class="review-quote">“All of his columns are amusing.<br>The best are masterpieces”</p>
      <footer class="review-source">- <cite>Harbour Ledger</cite></footer>
    </blockquote>
  </main>
</body>
</html>
```